RW Frameworks Inc Business cards

We need business cards using our existing logo but slightly modified. Right now the logo says RW Framework Masonry. We want to keep the RW part of the design, but replace the Framework Masonry portion with "FRAMEWORKS". Please see the attached file.
Ideally this would be a blank template so we can add Different Names, titles, and phone numbers later.
On the one side we want only the logo and on the other side the detail. I'm attaching an example for you to see.
Please reach out with any other questions. Our address and other details will be given out once we find a design we like.

Target Market(s)

Construction Industry

```html
<!DOCTYPE html>
<html lang="en">
<head>
<meta charset="utf-8">
<title>RW Frameworks Inc Business Cards</title>
<link href="https://fonts.googleapis.com/css2?family=Arimo:wght@400;700&display=swap" rel="stylesheet">
<style>
  :root {
    --brand-blue: #0f77be;
    --ink: #2b2b2b;
    --rule: #8a8a8a;
    --paper: #ffffff;
    --backdrop: #d6d6d6;
  }
  * { margin: 0; padding: 0; box-sizing: border-box; }
  html, body {
    width: 1125px;
    height: 1200px;
    overflow: hidden;
    background: var(--backdrop);
    font-family: "Arimo", Arial, sans-serif;
  }
  .canvas {
    position: relative;
    width: 1125px;
    height: 1200px;
  }
  .card {
    position: absolute;
    left: 112px;
    width: 900px;
    height: 512px;
    border-radius: 28px;
  }
  .card--front { top: 60px; background: var(--paper); }
  .card--back { top: 628px; background: var(--brand-blue); }

  .wordmark {
    position: absolute;
    display: flex;
    flex-direction: column;
    align-items: center;
    font-weight: 700;
    white-space: nowrap;
    line-height: 1;
  }
  .wordmark__initials { display: block; }
  .wordmark__name { display: block; }

  .card--front .wordmark {
    left: 141px;
    top: 192px;
    width: 271px;
    color: var(--brand-blue);
  }
  .card--front .wordmark__initials { font-size: 88px; letter-spacing: 2px; }
  .card--front .wordmark__name {
    margin-top: 14px;
    font-size: 19px;
    letter-spacing: 12px;
    margin-right: -12px;
  }

  .card--back .wordmark {
    left: 0;
    right: 0;
    top: 166px;
    color: var(--paper);
  }
  .card--back .wordmark__initials { font-size: 128px; letter-spacing: 3px; }
  .card--back .wordmark__name {
    margin-top: 20px;
    font-size: 25px;
    letter-spacing: 16px;
    margin-right: -16px;
  }

  .divider {
    position: absolute;
    left: 449px;
    top: 145px;
    width: 2px;
    height: 220px;
    background: var(--rule);
  }

  .details {
    position: absolute;
    left: 486px;
    top: 143px;
    color: var(--ink);
    font-size: 21px;
    line-height: 1.25;
  }
  .details__name {
    font-size: 31px;
    font-weight: 700;
    color: var(--brand-blue);
    line-height: 1.1;
  }
  .details__title { margin-top: 2px; }
  .details__address { margin-top: 12px; }
  .details__contacts { margin-top: 12px; list-style: none; }
  .details__contacts li {
    display: flex;
    align-items: center;
    gap: 7px;
    margin-bottom: 5px;
  }
  .icon { width: 17px; height: 17px; flex: none; }
</style>
</head>
<body>
<div class="canvas">

  <section class="card card--front" aria-label="Card front with contact details">
    <div class="wordmark">
      <span class="wordmark__initials">RW</span>
      <span class="wordmark__name">FRAMEWORKS</span>
    </div>
    <div class="divider"></div>
    <div class="details">
      <p class="details__name">GARRETT LANE</p>
      <p class="details__title">Owner/CEO</p>
      <p class="details__address">1450 W Ridge street<br>Harlow County 6417</p>
      <ul class="details__contacts">
        <li>
          <svg class="icon" viewBox="0 0 20 20" aria-hidden="true">
            <path fill="var(--brand-blue)" d="M4 2h4l1.5 4-2.3 1.6c1 2.2 2.8 4 5 5L13.8 10.4 18 12v4c0 1-1 2-2 2C8.3 17.6 2.4 11.7 2 4c0-1 1-2 2-2z"/>
          </svg>
          123-555-0187
        </li>
        <li>
          <svg class="icon" viewBox="0 0 20 20" aria-hidden="true">
            <rect x="1" y="4" width="18" height="12" fill="var(--brand-blue)"/>
            <path d="M1 4l9 7 9-7M1 16l7-6M19 16l-7-6" stroke="#fff" stroke-width="1.4" fill="none"/>
          </svg>
          info@rwframeworks.com
        </li>
        <li>
          <svg class="icon" viewBox="0 0 20 20" aria-hidden="true">
            <circle cx="10" cy="10" r="8.5" fill="var(--brand-blue)"/>
            <path d="M5 6c2 0 3 1 3 3s-2 2-2 4M12 3c0 2 2 3 4 3M13 17c0-3 1-4 3-5" stroke="#fff" stroke-width="1.6" fill="none"/>
          </svg>
          www.rwframeworks.com
        </li>
      </ul>
    </div>
  </section>

  <section class="card card--back" aria-label="Card back with company name">
    <div class="wordmark">
      <span class="wordmark__initials">RW</span>
      <span class="wordmark__name">FRAMEWORKS</span>
    </div>
  </section>

</div>
</body>
</html>
```